TBM Behaviours

As per attached we have a "Our Purpose" Ribbon and "Behaviors Supporting our Pursuit" slide Sketch Hive designed the logo for the Tormen Bluff Vision (Project ID 6184732 ), it would be good to get this built in professionally rather than just cut in as per attached. Like wise with the Tormen Bluff Mission.

Each Behavior would be as per design, with them Grouped as pictured, but also individual on separate slides, both with words and without allowing us to used them in many different formats.

From there some creativity to help us promote and deploy these to our business.

Target Market(s)

This is for our workforce

Requirements
Must have
• Include Our Purpose and The behaviors.

```html
<!DOCTYPE html>
<html lang="en">
<head>
<meta charset="utf-8">
<title>TBM Behaviours</title>
<link href="https://fonts.googleapis.com/css2?family=Poppins:wght@300;400;600;700&display=swap" rel="stylesheet">
<style>
  :root {
    --orange: #ff6f00;
    --green: #3ef39c;
    --green-text: #1fb86a;
    --violet: #d63df0;
    --sky: #56a5ea;
    --indigo: #5a22e6;
    --pink: #f52bc4;
    --grey-title: #a7a7a7;
    --grey-body: #9b9b9b;
    --ink: #555;
    --brand-blue: #0b3f94;
    --page: #ffffff;
  }
  * { margin: 0; padding: 0; box-sizing: border-box; }
  html, body { width: 1048px; height: 1200px; overflow: hidden; background: var(--page); }
  body { position: relative; font-family: "Poppins", sans-serif; }

  .slide {
    position: absolute; left: 62px; width: 926px; height: 514px;
    background: #fff;
    box-shadow: 3px 3px 4px rgba(0,0,0,0.45), 0 0 3px rgba(0,0,0,0.08);
  }
  .slide--purpose { top: 66px; }
  .slide--behaviours { top: 606px; }

  .slide-title {
    position: absolute; left: 30px; font-weight: 700; color: var(--grey-title);
    letter-spacing: -0.2px; line-height: 1;
  }
  .slide-title .accent { color: var(--orange); }
  .slide-title::after {
    content: ""; position: absolute; left: 0; bottom: -14px; height: 3px;
    background: var(--orange); width: var(--rule, 56px);
  }
  .slide--purpose .slide-title { top: 64px; font-size: 28px; --rule: 56px; }
  .slide--behaviours .slide-title { top: 38px; font-size: 28px; --rule: 162px; }

  .brand {
    position: absolute; right: 32px; bottom: 28px;
    font-weight: 600; font-size: 11px; color: var(--brand-blue); line-height: 1;
  }

  /* purpose cards */
  .card {
    position: absolute; top: 204px; width: 143px; height: 146px;
    border-radius: 14px; border: 2px solid #fff;
    background: linear-gradient(125deg, #dcdbe1 0%, #ecebef 55%, #ffffff 100%);
    box-shadow: 0 0 0 1px #e9e9ec, 0 10px 8px -6px rgba(0,0,0,0.25);
    text-align: center; padding: 36px 0 0;
  }
  .card .ribbon { position: absolute; top: -10px; left: 50%; transform: translateX(-50%); width: 82px; height: 26px; }
  .card-title { font-size: 12.5px; font-weight: 400; line-height: 1.2; white-space: nowrap; letter-spacing: -0.1px; }
  .card-title--bold { font-weight: 600; }
  .card-text { margin-top: 10px; font-size: 8.6px; font-weight: 300; color: var(--grey-body); line-height: 1.17; padding: 0 24px; }
  .card--orange { left: 32px; } .card--orange .card-title { color: var(--orange); }
  .card--green { left: 270px; } .card--green .card-title { color: var(--green); }
  .card--violet { left: 506px; } .card--violet .card-title { color: var(--violet); }
  .card--sky { left: 748px; } .card--sky .card-title { color: var(--sky); }

  /* behaviours */
  .chevron { position: absolute; width: 50px; height: 82px; }
  .step-no { position: absolute; font-size: 17px; font-weight: 400; line-height: 1; }
  .step-title { position: absolute; font-size: 14px; font-weight: 400; line-height: 1; white-space: nowrap; }
  .step-text { position: absolute; font-size: 6.6px; color: var(--ink); line-height: 1.2; }
</style>
</head>
<body>

<section class="slide slide--purpose">
  <h1 class="slide-title"><span class="accent">Our</span> Purpose</h1>

  <article class="card card--orange">
    <svg class="ribbon" viewBox="0 0 82 26"><polygon points="6,0 76,0 82,8 66,8 41,25 16,8 0,8" fill="var(--orange)"/><polygon points="0,8 6,0 8,8" fill="#c24f00"/><polygon points="82,8 76,0 74,8" fill="#c24f00"/></svg>
    <h2 class="card-title">Northvale’s Purpose</h2>
    <p class="card-text">To bring people and resources together to build a better world.</p>
  </article>

  <article class="card card--green">
    <svg class="ribbon" viewBox="0 0 82 26"><polygon points="6,0 76,0 82,8 66,8 41,25 16,8 0,8" fill="var(--green)"/><polygon points="0,8 6,0 8,8" fill="#1f9e62"/><polygon points="82,8 76,0 74,8" fill="#1f9e62"/></svg>
    <h2 class="card-title card-title--bold">Tormen Bluff Vision</h2>
    <p class="card-text">Vision aligns you with your goals and the destination you’re moving towards.</p>
  </article>

  <article class="card card--violet">
    <svg class="ribbon" viewBox="0 0 82 26"><polygon points="6,0 76,0 82,8 66,8 41,25 16,8 0,8" fill="var(--violet)"/><polygon points="0,8 6,0 8,8" fill="#8f1ea3"/><polygon points="82,8 76,0 74,8" fill="#8f1ea3"/></svg>
    <h2 class="card-title">Tormen Bluff Mission</h2>
    <p class="card-text">Mission empowers you with the actions to accomplish your vision.</p>
  </article>

  <article class="card card--sky">
    <svg class="ribbon" viewBox="0 0 82 26"><polygon points="6,0 76,0 82,8 66,8 41,25 16,8 0,8" fill="var(--sky)"/><polygon points="0,8 6,0 8,8" fill="#2f77b8"/><polygon points="82,8 76,0 74,8" fill="#2f77b8"/></svg>
    <h2 class="card-title">Tormen Bluff Mission</h2>
    <p class="card-text">Mission empowers you with the actions to accomplish your vision.</p>
  </article>

  <div class="brand">Northvale Alliance</div>
</section>

<section class="slide slide--behaviours">
  <h1 class="slide-title"><span class="accent">Behaviours</span> Supporting our Pursuit</h1>

  <svg class="chevron" style="left:166px;top:182px" viewBox="0 0 50 82"><polygon points="22,0 50,0 14,41 50,82 22,82 0,41" fill="var(--green)"/><polygon points="44,0 50,0 14,41 50,82 44,82 10,41" fill="#2cc27c"/></svg>
  <span class="step-no" style="left:204px;top:215px;color:var(--green)">01</span>
  <h3 class="step-title" style="left:236px;top:184px;color:var(--green-text)">Enjoy What we do</h3>
  <p class="step-text" style="left:238px;top:206px;width:84px">We all create a fun and enjoyable work environment that people are proud of.</p>

  <svg class="chevron" style="left:201px;top:280px" viewBox="0 0 50 82"><g transform="translate(50,0) scale(-1,1)"><polygon points="22,0 50,0 14,41 50,82 22,82 0,41" fill="var(--orange)"/><polygon points="44,0 50,0 14,41 50,82 44,82 10,41" fill="#c25200"/></g></svg>
  <span class="step-no" style="left:195px;top:314px;color:var(--orange)">02</span>
  <h3 class="step-title" style="left:63px;top:282px;color:var(--orange)">Value Diversity</h3>
  <p class="step-text" style="left:63px;top:305px;width:130px">We all different backgrounds and experience, and enabling our teams success. We promote an environment where you can be 100% yourself.</p>

  <svg class="chevron" style="left:449px;top:182px" viewBox="0 0 50 82"><polygon points="22,0 50,0 14,41 50,82 22,82 0,41" fill="var(--violet)"/><polygon points="44,0 50,0 14,41 50,82 44,82 10,41" fill="#9221a8"/></svg>
  <span class="step-no" style="left:483px;top:215px;color:var(--violet)">03</span>
  <h3 class="step-title" style="left:518px;top:184px;color:var(--violet);font-size:15px">Focus on Quality</h3>
  <p class="step-text" style="left:520px;top:206px;width:104px">Everyone strives for quality outcomes by removing waste, rework and frustration.</p>

  <svg class="chevron" style="left:487px;top:280px" viewBox="0 0 50 82"><g transform="translate(50,0) scale(-1,1)"><polygon points="22,0 50,0 14,41 50,82 22,82 0,41" fill="var(--indigo)"/><polygon points="44,0 50,0 14,41 50,82 44,82 10,41" fill="#3a12a6"/></g></svg>
  <span class="step-no" style="left:481px;top:314px;color:var(--indigo)">04</span>
  <h3 class="step-title" style="left:340px;top:284px;color:var(--indigo);font-size:15px">Teamwork</h3>
  <p class="step-text" style="left:340px;top:307px;width:136px">Making tomorrow better than today by continuously improving, working as 1Team, sharing, leveraging our strengths and celebrating our successes.</p>

  <svg class="chevron" style="left:711px;top:182px" viewBox="0 0 50 82"><polygon points="22,0 50,0 14,41 50,82 22,82 0,41" fill="var(--sky)"/><polygon points="44,0 50,0 14,41 50,82 44,82 10,41" fill="#2f7cc1"/></svg>
  <span class="step-no" style="left:745px;top:215px;color:var(--sky)">05</span>
  <h3 class="step-title" style="left:780px;top:184px;color:var(--sky);font-size:15px">Caring</h3>
  <p class="step-text" style="left:781px;top:202px;width:100px">We are genuinely interested in the safety and wellbeing of all our people, we respect each other and always feel safe to speak up.</p>

  <svg class="chevron" style="left:749px;top:280px" viewBox="0 0 50 82"><g transform="translate(50,0) scale(-1,1)"><polygon points="22,0 50,0 14,41 50,82 22,82 0,41" fill="var(--pink)"/><polygon points="44,0 50,0 14,41 50,82 44,82 10,41" fill="#b0168b"/></g></svg>
  <span class="step-no" style="left:743px;top:314px;color:var(--pink)">06</span>
  <h3 class="step-title" style="left:612px;top:284px;color:var(--pink);font-size:13px">Serve our Customer</h3>
  <p class="step-text" style="left:612px;top:312px;width:114px">We know who our customers are and regularly check on how we are delivering to their needs.</p>

  <div class="brand">Northvale Alliance</div>
</section>

</body>
</html>
```